Quillmark Select

Letter Head, Envelope, Business Cards, Social Media Banner (FB/Twitter), Social Media Icon, Social Media Announcement Template...

We are a Softball Team/Organization

Target Market(s)

High School Student-Athletes (softball players) and their parents

Font styles to use
Serif

Requirements
Must have
• Logo & Colors
Must POP and say WOW
Common theme amongst all designs

```html
<!DOCTYPE html>
<html lang="en">
<head>
<meta charset="UTF-8">
<title>Quillmark Select — Envelope Set</title>
<link rel="stylesheet" href="https://fonts.googleapis.com/css2?family=Roboto:wght@400;700&display=swap">
<style>
  :root {
    --navy: #2b3f61;
    --steel: #a5adb9;
    --paper: #f3f3f4;
    --ground: #e8e8e9;
    --ink-grey: #5a5d63;
    --mark-light: #c9ced7;
  }
  * { margin: 0; padding: 0; box-sizing: border-box; }
  html, body {
    width: 1200px; height: 795px; overflow: hidden;
    background: var(--ground);
    font-family: "Roboto", Arial, sans-serif;
  }
  .canvas { position: relative; width: 1200px; height: 795px; }

  .envelope {
    position: absolute;
    width: 560px; height: 280px;
    background: var(--paper);
    box-shadow: 0 6px 18px rgba(0,0,0,0.12);
    overflow: hidden;
  }

  /* Back of envelope */
  .envelope--back { left: 590px; top: 60px; }
  .envelope__flap {
    position: absolute; left: 0; top: 0; width: 100%; height: 92px;
    background: var(--navy);
    border-radius: 0 0 14px 14px;
    display: flex; align-items: center; justify-content: center;
  }
  .wordmark {
    display: flex; align-items: center; gap: 9px;
    font-weight: 700; letter-spacing: 0.04em; line-height: 1;
  }
  .wordmark__dot { width: 12px; height: 12px; border-radius: 50%; background: currentColor; }
  .envelope__flap .wordmark { color: var(--mark-light); font-size: 22px; }
  .return-address {
    position: absolute; left: 70px; top: 122px;
    font-size: 13px; line-height: 1.45; color: var(--ink-grey);
  }
  .return-address__name { color: var(--navy); }

  /* Front of envelope */
  .envelope--front { left: 60px; top: 420px; }
  .envelope__logo { position: absolute; left: 44px; top: 40px; }
  .envelope__logo .wordmark { color: var(--navy); font-size: 24px; }
  .envelope__stripe {
    position: absolute; left: 0; bottom: 0; width: 280px; height: 14px;
    background: var(--steel);
  }
  .envelope__tab { position: absolute; right: 0; bottom: 0; width: 300px; height: 40px; }
  .envelope__url {
    position: absolute; right: 26px; bottom: 11px;
    font-size: 16px; color: #ffffff; letter-spacing: 0.02em;
  }
</style>
</head>
<body>
<div class="canvas">

  <section class="envelope envelope--back" aria-label="Envelope back">
    <div class="envelope__flap">
      <div class="wordmark"><span class="wordmark__dot"></span>QUILLMARK SELECT</div>
    </div>
    <address class="return-address" style="font-style:normal">
      <div class="return-address__name">Quillmark Select LTD.</div>
      <div>2175 Harlow Field Lane Brookvale, Oh 45210</div>
    </address>
  </section>

  <section class="envelope envelope--front" aria-label="Envelope front">
    <div class="envelope__logo">
      <div class="wordmark"><span class="wordmark__dot"></span>QUILLMARK SELECT</div>
    </div>
    <div class="envelope__stripe"></div>
    <svg class="envelope__tab" viewBox="0 0 300 40" preserveAspectRatio="none" aria-hidden="true">
      <polygon points="28,0 300,0 300,40 0,40 0,14" fill="var(--navy)"/>
    </svg>
    <span class="envelope__url">www.quillmarkselect.com</span>
  </section>

</div>
</body>
</html>
```